50-60's Rock singer' 'Only a voice and a song' show add for poster etc

The singer's name is Dewey Hart.

He is the only one of the 3 major superstars of the late 50's early 60's original Rock'n'Roll era who still performing. He is 'The Last man standing from his era'. and this show is called, 'Only a voice and a song'.

The show is a one man show where he sings his own Gold Hits, tells stories about his career and sings the biggest hits of that era, that his friends recorded.
It also features a special a special Audio Visual show to relive the 50's and 60's.
Up until this show, the well known singer had always performed with his band, so there may be an expectation that they will be here on this show.

There is no band however the music featured is the best Rock'n'Roll available.
I'd be interested in seeing your initial ideas so we can work through them.
I don't see it as being too busy although I am open to suggestions.
Just some photos attached but many other available.
You can Searcha and Vidstream his name if you need more info.
Updates

Hi guys, Update. Sorry, but somehow the singer's name was left out of the brief.. It is Dewey Hart. Many thanks for the ideas thus far. You are all very talented. I have attached some more photos and a couple of ideas that have been used with Carlo and Benny images.

Target Market(s)

Theatres. clubs, demographic 55 up - Rockabilly, Fifties Rock'n'Roll (Early Carlo era)

Industry/Entity Type

Entertainment

Requirements
Must have
• Dewey Hart -name, Last man Standing from his era - sub title, Only a voice and a song -show title
Nice to have
• The ideas of the Carlo and Benny images are nice and could be used. If the image in the blue shirt (20220325_111431-cropped.jpg) is used, thicken the hair so one cannot see through it.
Should not have
• NO dates, times, venues etc

```html
<!DOCTYPE html>
<html lang="en">
<head>
<meta charset="utf-8">
<title>Dewey Hart – Only a voice and a song – poster versions</title>
<link rel="stylesheet" href="https://fonts.googleapis.com/css2?family=Josefin+Sans:wght@600;700&family=Montserrat:wght@800;900&family=Kaushan+Script&family=Mr+Dafoe&family=Oswald:wght@500&display=swap">
<style>
  :root {
    --board: #5a5a5a;
    --frame: #fbf6e6;
    --poster-black: #111111;
    --cream: #f3e2c4;
    --white: #ffffff;
    --label-grey: #9c9c9c;
    --photo-light: #e8d6b8;
    --photo-mid: #8a7b69;
    --photo-smoke: #6e6e6e;
  }
  * { margin: 0; padding: 0; box-sizing: border-box; }
  html, body { width: 1200px; height: 614px; overflow: hidden; }
  body { background: var(--board); position: relative; font-family: "Josefin Sans", sans-serif; }

  .version { position: absolute; top: 44px; width: 330px; }
  .version--one { left: 54px; }
  .version--two { left: 435px; }
  .version--three { left: 817px; }

  .poster {
    position: relative;
    width: 330px; height: 467px;
    background: var(--poster-black);
    border: 7px solid var(--frame);
    box-shadow: 8px 10px 14px rgba(0,0,0,0.45);
    overflow: hidden;
  }

  .poster__name {
    position: absolute; left: 0; right: 0; top: 22px;
    text-align: center; color: var(--cream);
    font: 700 21px/1 "Josefin Sans", sans-serif; letter-spacing: 6px;
  }
  .poster__tagline {
    position: absolute; left: 0; right: 0; top: 47px;
    text-align: center; color: var(--white);
    font: 600 11px/1 "Josefin Sans", sans-serif; letter-spacing: 1.6px;
  }

  .poster__photo {
    position: absolute; left: 32px; top: 62px; width: 268px; height: 262px;
    border-radius: 46% 42% 38% 44% / 40% 46% 36% 42%;
    background:
      radial-gradient(ellipse 38% 42% at 42% 45%, var(--photo-light) 0%, rgba(232,214,184,0.55) 45%, transparent 75%),
      radial-gradient(ellipse 60% 55% at 60% 40%, var(--photo-smoke) 0%, rgba(110,110,110,0.4) 55%, transparent 80%),
      radial-gradient(ellipse 55% 45% at 50% 80%, var(--photo-mid) 0%, transparent 75%);
  }

  .title-block { position: absolute; left: 0; right: 0; }
  .title__lead, .title__script { white-space: nowrap; }

  /* Version 1 */
  .version--one .title-block { top: 330px; height: 112px; }
  .version--one .title__lead {
    position: absolute; left: 104px; top: 12px;
    color: var(--white); font: 900 17px/1 "Montserrat", sans-serif; letter-spacing: 0.3px;
  }
  .version--one .title__script {
    position: absolute; left: 26px; top: 22px;
    color: var(--cream); font: 400 76px/1 "Kaushan Script", cursive;
  }

  /* Version 2 */
  .version--two .title-block { top: 322px; height: 120px; }
  .version--two .title__lead {
    position: absolute; left: 104px; top: 0;
    color: var(--white); font: 400 32px/1 "Mr Dafoe", cursive;
  }
  .version--two .title__script {
    position: absolute; left: 26px; top: 36px;
    color: var(--cream); font: 400 76px/1 "Kaushan Script", cursive;
  }

  /* Version 3 */
  .version--three .poster__name { top: 32px; }
  .version--three .poster__tagline { top: 57px; }
  .version--three .poster__photo { top: 82px; height: 272px; }
  .version--three .title-block { top: 360px; text-align: center; }
  .version--three .title__lead {
    display: block; color: var(--white);
    font: 900 21px/1 "Montserrat", sans-serif; letter-spacing: 0.3px;
  }
  .version--three .title__script {
    display: block; margin-top: 4px; color: var(--cream);
    font: 900 50px/1 "Montserrat", sans-serif; letter-spacing: 1px;
  }

  .version__label {
    margin-top: 35px; text-align: center; color: var(--label-grey);
    font: 500 34px/1 "Oswald", sans-serif; letter-spacing: 3px;
  }
</style>
</head>
<body>

  <section class="version version--one">
    <div class="poster">
      <div class="poster__name">DEWEY HART</div>
      <div class="poster__tagline">LAST MAN STANDING FROM HIS ERA</div>
      <div class="poster__photo" role="img" aria-label="Sepia photo of the singer singing into a vintage microphone over a grey smoke splash"></div>
      <div class="title-block">
        <span class="title__lead">ONLY A VOICE AND</span>
        <span class="title__script">A song</span>
      </div>
    </div>
    <div class="version__label">VERSION 1</div>
  </section>

  <section class="version version--two">
    <div class="poster">
      <div class="poster__name">DEWEY HART</div>
      <div class="poster__tagline">LAST MAN STANDING FROM HIS ERA</div>
      <div class="poster__photo" role="img" aria-label="Sepia photo of the singer singing into a vintage microphone over a grey smoke splash"></div>
      <div class="title-block">
        <span class="title__lead">Only a voice and</span>
        <span class="title__script">A song</span>
      </div>
    </div>
    <div class="version__label">VERSION 2</div>
  </section>

  <section class="version version--three">
    <div class="poster">
      <div class="poster__name">DEWEY HART</div>
      <div class="poster__tagline">LAST MAN STANDING FROM HIS ERA</div>
      <div class="poster__photo" role="img" aria-label="Sepia photo of the singer singing into a vintage microphone over a grey smoke splash"></div>
      <div class="title-block">
        <span class="title__lead">ONLY A VOICE AND</span>
        <span class="title__script">A SONG</span>
      </div>
    </div>
    <div class="version__label">VERSION 3</div>
  </section>

</body>
</html>
```